Haverlund’s First Annual Tree Fort Poker Tournament

Need a flyer made up of all the details. I like this tree fort image I uploaded with maybe 4-5 guys hanging out holding cards with some poker chips flying around. The name of it above it and then have the date, food provided over $10,000 in prize money, $500 buy in. Saturday December 17th, noon - ? 1/2 due by October 1 rest due day of tournament. Then have my contact info along with the guy helping me. Gregory Haverlund 314-617-3042 or Marcus Tredwin 314-586-2197

```html
<!DOCTYPE html>
<html lang="en">
<head>
<meta charset="utf-8">
<title>Haverlund’s First Annual Tree Fort Poker Tournament</title>
<link href="https://fonts.googleapis.com/css2?family=Oswald:wght@700&family=Titan+One&family=Poppins:wght@400;500;600;700&display=swap" rel="stylesheet">
<style>
  :root {
    --page: #ffffff;
    --sky-top: #b3e6fc;
    --sky-bottom: #8ad2f2;
    --red: #d60d10;
    --deep-red: #9e0d0d;
    --brown: #4a1e08;
    --wood: #9a5217;
    --wood-dark: #5c2c08;
    --navy: #1f2340;
    --ink: #2a1a12;
    --gold: #ffd21f;
    --white: #ffffff;
  }
  * { margin: 0; padding: 0; box-sizing: border-box; }
  html, body { width: 1200px; height: 3193px; overflow: hidden; background: var(--page); }
  .flyer {
    position: absolute; left: 50px; top: 819px; width: 1100px; height: 1555px;
    background: linear-gradient(180deg, var(--sky-top), var(--sky-bottom));
    box-shadow: 0 20px 60px rgba(0,0,0,0.22);
    text-align: center; overflow: hidden;
  }
  .row { position: absolute; left: 0; width: 100%; }
  .title-lead {
    top: 52px; font-family: "Oswald", sans-serif; font-weight: 700;
    font-size: 96px; line-height: 1; color: var(--red); letter-spacing: -1px;
    text-transform: uppercase;
  }
  .title-main {
    top: 168px; font-family: "Titan One", sans-serif; font-size: 142px; line-height: 1;
    color: var(--wood); letter-spacing: 4px; word-spacing: 30px;
    -webkit-text-stroke: 3px var(--wood-dark);
  }
  .title-sub {
    top: 330px; font-family: "Poppins", sans-serif; font-weight: 700; font-size: 84px;
    line-height: 1; color: var(--brown); display: flex; justify-content: center; align-items: center;
  }
  .chip { width: 72px; height: 72px; margin: 0 2px; }
  .scene-art {
    top: 450px; left: 70px; width: 960px; height: 710px;
    background: radial-gradient(ellipse at 50% 45%, #6cbf3c 0%, #8fcf64 30%, #a9dcf3 62%, rgba(140,210,242,0) 75%);
    border-radius: 40px;
  }
  .date-pill {
    top: 1216px; left: 50%; transform: translateX(-50%); width: auto;
    background: var(--white); border-radius: 14px; padding: 2px 18px;
    font-family: "Poppins", sans-serif; font-weight: 700; font-size: 36px; color: var(--ink);
    white-space: nowrap; line-height: 1.3;
  }
  .date-pill .accent { color: var(--red); }
  .date-pill sup { font-size: 20px; }
  .schedule {
    top: 1276px; font-family: "Poppins", sans-serif; font-weight: 500; font-size: 24px; color: var(--ink);
  }
  .prize-pill {
    top: 1314px; left: 50%; transform: translateX(-50%); width: auto;
    background: var(--deep-red); border-radius: 12px; padding: 2px 22px;
    font-family: "Poppins", sans-serif; font-weight: 700; font-size: 29px; color: var(--white);
    white-space: nowrap; line-height: 1.45;
  }
  .prize-pill .amount { color: var(--gold); }
  .prize-pill .amount small { font-size: 19px; vertical-align: 4px; }
  .prize-line {
    top: 1360px; font-family: "Poppins", sans-serif; font-weight: 700; font-size: 29px; color: var(--navy);
  }
  .prize-line .accent { color: var(--red); }
  .divider { top: 1420px; left: 170px; width: 760px; height: 1px; background: rgba(31,35,64,0.25); }
  .contacts {
    top: 1446px; display: flex; justify-content: center; align-items: center; gap: 10px;
    font-family: "Poppins", sans-serif; font-weight: 700; font-size: 19px; color: var(--ink);
    text-transform: uppercase; white-space: nowrap;
  }
  .contacts .or { font-weight: 400; margin: 0 10px; }
  .phone-tag {
    display: inline-flex; align-items: center; gap: 5px;
    background: var(--deep-red); color: var(--white); border-radius: 5px;
    padding: 1px 10px; border: 1px solid var(--white);
  }
  .phone-tag svg { width: 15px; height: 15px; }
</style>
</head>
<body>
  <main class="flyer">
    <h1 class="row title-lead">Haverlund’s First Annual</h1>
    <div class="row title-main">TREE FORT</div>
    <div class="row title-sub">
      <span>P</span>
      <svg class="chip" viewBox="0 0 72 72" aria-hidden="true">
        <circle cx="36" cy="36" r="34" fill="#d60d10"/>
        <g stroke="#ffffff" stroke-width="8">
          <line x1="36" y1="2" x2="36" y2="13"/><line x1="36" y1="59" x2="36" y2="70"/>
          <line x1="2" y1="36" x2="13" y2="36"/><line x1="59" y1="36" x2="70" y2="36"/>
          <line x1="12" y1="12" x2="19.8" y2="19.8"/><line x1="52.2" y1="52.2" x2="60" y2="60"/>
          <line x1="60" y1="12" x2="52.2" y2="19.8"/><line x1="19.8" y1="52.2" x2="12" y2="60"/>
        </g>
        <circle cx="36" cy="36" r="20" fill="#ffffff"/>
        <circle cx="36" cy="36" r="16" fill="#d60d10"/>
      </svg>
      <span>KER TOURNAMENT</span>
    </div>

    <div class="row scene-art" role="img" aria-label="Illustration of a tree fort on a grassy island surrounded by water, with people holding giant playing cards and poker chips flying around"></div>

    <div class="row date-pill">SATURDAY <span class="accent">DECEMBER 17<sup>TH</sup></span></div>
    <p class="row schedule">noon&nbsp; 1/2 due by October 1 rest due day of tournament</p>
    <div class="row prize-pill">FOOD PROVIDED OVER <span class="amount"><small>$</small>10,000</span></div>
    <p class="row prize-line">IN PRIZE MONEY, <span class="accent">$500</span> BUY IN</p>
    <div class="row divider"></div>

    <div class="row contacts">
      <span>Gregory Haverlund</span>
      <span class="phone-tag">
        <svg viewBox="0 0 24 24" aria-hidden="true"><path fill="#ffffff" d="M6.6 10.8c1.4 2.8 3.8 5.1 6.6 6.6l2.2-2.2c.3-.3.7-.4 1-.2 1.1.4 2.3.6 3.6.6.6 0 1 .4 1 1V20c0 .6-.4 1-1 1C10.6 21 3 13.4 3 4c0-.6.4-1 1-1h3.5c.6 0 1 .4 1 1 0 1.3.2 2.5.6 3.6.1.3 0 .7-.2 1l-2.3 2.2z"/></svg>
        314-617-3042
      </span>
      <span class="or">OR</span>
      <span>Marcus Tredwin</span>
      <span class="phone-tag">
        <svg viewBox="0 0 24 24" aria-hidden="true"><path fill="#ffffff" d="M6.6 10.8c1.4 2.8 3.8 5.1 6.6 6.6l2.2-2.2c.3-.3.7-.4 1-.2 1.1.4 2.3.6 3.6.6.6 0 1 .4 1 1V20c0 .6-.4 1-1 1C10.6 21 3 13.4 3 4c0-.6.4-1 1-1h3.5c.6 0 1 .4 1 1 0 1.3.2 2.5.6 3.6.1.3 0 .7-.2 1l-2.3 2.2z"/></svg>
        314-586-2197
      </span>
    </div>
  </main>
</body>
</html>
```